Introduction of new dentist and new treatments

We want inform our Patients of our new dentist and new treatment methods. It is dealing about biologic dentistry and holistic dentistry. we are in switzerland and speak german

Font styles to use
Sans Serif

Colors
00a990
33b8a4
9bcb3c
acd036
cadf82
0292cd
3176b5
e34297
e667a6

Requirements
Must have
• Text, which can be edited. It will be in german
• Name of the dental clinic is
• "Velmora - Ihr Zahnarzt in Zug"
Nice to have
• A4 Layout

```html
<!DOCTYPE html>
<html lang="de">
<head>
<meta charset="utf-8">
<title>Velmora – Ihr Zahnarzt in Zug</title>
<link href="https://fonts.googleapis.com/css2?family=Open+Sans:wght@400;600&family=Roboto+Slab:wght@500&display=swap" rel="stylesheet">
<style>
  :root {
    --backdrop: #9fd3e8;
    --paper: #ffffff;
    --navy: #1c2f5e;
    --blue: #0292cd;
    --blue-deep: #3176b5;
    --sky: #29a8e0;
    --green: #2fae3a;
    --lime: #9bcb3c;
    --text: #3a3a3a;
  }
  * { margin: 0; padding: 0; box-sizing: border-box; }
  html, body { width: 768px; height: 1200px; overflow: hidden; }
  body { background: var(--backdrop); font-family: "Open Sans", sans-serif; }

  .flyer {
    position: absolute; left: 34px; top: 105px;
    width: 700px; height: 990px;
    background: var(--paper); overflow: hidden;
  }
  .flyer-header { position: absolute; left: 0; top: 0; width: 700px; height: 402px; }

  .brand {
    position: absolute; left: 38px; top: 322px;
    display: flex; flex-direction: column; align-items: flex-start;
  }
  .brand-row { display: flex; align-items: center; gap: 10px; }
  .brand-mark {
    width: 14px; height: 14px; border-radius: 50%;
    background: var(--blue);
  }
  .brand-name {
    font-family: "Open Sans", sans-serif; font-weight: 600;
    font-size: 26px; line-height: 30px; color: var(--navy);
  }
  .brand-tagline {
    font-family: "Open Sans", sans-serif; font-weight: 600;
    font-size: 11px; color: var(--navy); margin-top: 2px; margin-left: 24px;
  }

  .content {
    position: absolute; left: 38px; top: 388px; width: 624px;
  }
  .section { margin-bottom: 16px; }
  .section-title {
    font-family: "Roboto Slab", serif; font-weight: 500;
    font-size: 16px; line-height: 21px; color: var(--blue-deep);
    text-decoration: underline; text-underline-offset: 2px;
    margin-bottom: 7px;
  }
  .section-title .lead { color: var(--green); }
  .section p {
    font-size: 11.2px; line-height: 15.4px; color: var(--text);
    text-align: justify;
  }
  .section p + p { margin-top: 9px; }

  .footer-line { position: absolute; left: 0; top: 960px; width: 700px; height: 4px; background: var(--green); }
  .footer-band { position: absolute; left: 0; top: 968px; width: 700px; height: 22px; background: var(--navy); }
</style>
</head>
<body>
  <main class="flyer">
    <svg class="flyer-header" viewBox="0 0 505 290" preserveAspectRatio="none">
      <defs>
        <linearGradient id="photoTone" x1="0" y1="0" x2="1" y2="1">
          <stop offset="0" stop-color="#dfe6ea"/>
          <stop offset="0.5" stop-color="#eef1f3"/>
          <stop offset="1" stop-color="#cfdde6"/>
        </linearGradient>
      </defs>
      <rect role="img" aria-label="Foto: Zahnarztpraxis mit Patient auf dem Behandlungsstuhl, Zahnarzt im Gespräch und neuer Zahnarzt im blauen Poloshirt" x="0" y="0" width="505" height="290" fill="url(#photoTone)"/>
      <path d="M330,200 C400,150 450,120 505,110 L505,290 L330,290 Z" fill="var(--sky)"/>
      <path d="M0,205 C110,150 240,150 330,200 C400,240 450,250 505,238 L505,290 L0,290 Z" fill="var(--lime)"/>
      <path d="M0,212 C110,158 240,158 330,206 C400,246 450,256 505,246 L505,290 L0,290 Z" fill="var(--navy)"/>
      <path d="M0,175 C60,165 110,185 160,210 C230,240 260,225 310,215 C380,202 440,245 505,262 L505,290 L0,290 Z" fill="var(--blue)"/>
      <path d="M0,195 C60,190 110,205 160,228 C230,258 270,238 320,228 C390,216 440,254 505,272 L505,290 L0,290 Z" fill="var(--paper)"/>
    </svg>

    <div class="brand">
      <div class="brand-row">
        <span class="brand-mark"></span>
        <span class="brand-name">Velmora</span>
      </div>
      <span class="brand-tagline">Ihr Zahnarzt in Zug</span>
    </div>

    <div class="content">
      <section class="section">
        <h2 class="section-title"><span class="lead">Interdisziplinäre Zahnmedizin –</span><br>Zusammenhang zwischen Zahnproblemen und der Gesundheit von Körper</h2>
        <p>Zahn und Gesundheit haben eins gemeinsam – Man vermisst sie, wenn sie fehlt. Zähne haben einen engen Zusammenhang zur Gesundheit und können diese beeinflussen. Sowohl negativ als auch positiv.</p>
      </section>

      <section class="section">
        <h2 class="section-title"><span class="lead">Funktion des Kauorgans</span> und interdisziplinäre Zahnmedizin</h2>
        <p>Funktion ist nicht alles. Aber ohne Funktion ist alles nichts!“ Sagte einst Prof. A. Lindner (Zahnarzt, Gnathologie) und betonte die Bedeutung der Funktion des Kausystems.</p>
        <p>Sprechen, Kauen aber auch Körperhaltung und Stressmanagement gehören zu den Funktionen der Zähne. Ein gut funktionierendes Kauorgan (nach Prof. R. Haberl, interdisziplinäre Zahnmedizin) kann Stress bewältigen und mehr Leistung und Wohlbefinden bringen. Sehr oft erkennt man Funktionsstörungen daran, dass die Zähne nicht richtig zueinander passen oder Muskelverspannungen und Schmerzen im Kiefergelenk auftreten.</p>
      </section>

      <section class="section">
        <h2 class="section-title"><span class="lead">Zahnverlust</span> und neurologische Auswirkung</h2>
        <p>Ein physiologisches Kausystem hat sehr feine Steuerungs- und Wahrnehmungsmöglichkeiten. Bei Zahnverlust werden diese Fähigkeiten weniger benötigt. Weniger gebrauchte Ressourcen werden von der Natur dementsprechend abgebaut. Studien zeigen, dass Menschen mit weniger Zähnen mehr Risiko zur Bildung von Demenz haben.</p>
      </section>

      <section class="section">
        <h2 class="section-title"><span class="lead">Parodontitis</span> und systemische Erkrankungen</h2>
        <p>Parodontitis (Entzündung des Zahnhalteapparats) ist eine der häufigsten chronischen Krankheiten weltweit und daher gut erforscht. Herzkrankheiten, Diabetes und Frühgeburtlichkeit sind einige der systemischen Krankheiten mit der Parodontitis in Zusammenhang steht. Zahnfleischbulten, Zahnlockerung, Zahnfleischschwund und Zahnverlust sind typische Begleiterscheinungen von Parodontitis. Eine systematische Parodontitis-Behandlung kann auch positive Auswirkungen auf die gesamte Gesundheit haben.</p>
      </section>

      <section class="section">
        <h2 class="section-title"><span class="lead">Ganzheitliche Erklärungen</span></h2>
        <p>Die komplementäre Zahnheilkunde, sehr oft auch als ganzheitliche oder biologische Zahnheilkunde bezeichnet, versucht mit Hilfe von Meridianen (Traditionelle Chinesische Medizin), den Zusammenhang zwischen Zähnen und anderen Organen und Körperteilen zu erklären. Es gibt immer mehr Patienten und Zahnärzte die von dieser Theorie und deren Ergebnissen überzeugt sind. Aufgrund der wissenschaftlichen Lage ist eine ausführliche Aufklärung vor der Behandlung sehr ratsam.</p>
      </section>
    </div>

    <div class="footer-line"></div>
    <div class="footer-band"></div>
  </main>
</body>
</html>
```